Glimmora Pages with Bold Font

I want the font to be simple yet bold for Glimmora images. Its all about a simple bold readable font. I need a single glimmora page with an image and copy/text on or over the image. The words will change in the future. I'm looking for the right font. I like fiery red and yellow colors. The "One Pic" attached is a sample of what I want without the Veltrix words.

```html
<!DOCTYPE html>
<html lang="en">
<head>
<meta charset="utf-8">
<title>Glimmora Fitness Promo</title>
<link href="https://fonts.googleapis.com/css2?family=Poppins:wght@700;800&display=swap" rel="stylesheet">
<style>
  :root {
    --page: #ffffff;
    --ink-dark: #1a0a0b;
    --ink-deep: #230d0e;
    --fiery-red: #ee1c1c;
    --grunge-red: #a3141a;
    --headline-white: #ffffff;
    --paper: #f1ebdd;
    --paper-shadow: #d9d0bd;
    --body-ink: #2b2b2b;
    --photo-light: #e9c6b6;
    --photo-mid: #c99684;
    --photo-dark: #8e5f52;
  }
  * { box-sizing: border-box; margin: 0; padding: 0; }
  html, body {
    width: 1200px; height: 1200px; overflow: hidden;
    background: var(--page);
    font-family: "Poppins", Arial, sans-serif;
  }
  .promo {
    position: absolute; left: 44px; top: 50px;
    width: 1112px; height: 1112px;
    background: radial-gradient(ellipse at 70% 40%, var(--ink-deep), var(--ink-dark) 75%);
    overflow: hidden;
  }
  .grunge-band {
    position: absolute; right: 0; top: 0; width: 640px; height: 110px;
    background:
      repeating-linear-gradient(90deg, transparent 0 7px, rgba(163,20,26,.55) 7px 9px, transparent 9px 19px),
      linear-gradient(180deg, var(--grunge-red) 0%, rgba(163,20,26,.45) 35%, transparent 100%);
    opacity: .85;
  }
  .model-photo {
    position: absolute; left: 0; top: 0; width: 515px; height: 860px;
    background: linear-gradient(160deg, var(--photo-light) 0%, var(--photo-mid) 55%, var(--photo-dark) 100%);
  }
  .headline {
    position: absolute; right: 62px; top: 108px; width: 640px;
    text-align: right; color: var(--headline-white);
    font-weight: 800; font-size: 70px; line-height: 89px;
    text-transform: uppercase; letter-spacing: -0.5px;
  }
  .headline .hot { color: var(--fiery-red); }
  .paper {
    position: absolute; left: 0; top: 790px; width: 1112px; height: 322px;
  }
  .paper svg { position: absolute; left: 0; top: 0; }
  .paper-copy {
    position: absolute; left: 60px; right: 60px; top: 128px;
    text-align: center;
  }
  .paper-copy .intro {
    color: var(--body-ink); font-weight: 700; font-size: 21px; line-height: 33px;
  }
  .paper-copy .pitch {
    margin-top: 8px;
    color: var(--fiery-red); font-weight: 700; font-size: 25px; line-height: 42px;
  }
</style>
</head>
<body>
  <main class="promo">
    <div class="grunge-band"></div>
    <div class="model-photo" role="img" aria-label="Photo of a blonde woman posing, cropped at the torso"></div>

    <h1 class="headline">
      Helping more<br>guys get<br><span class="hot">hot, sweaty &amp;</span><br><span class="hot">hard</span> than a<br>Vegas hooker<br>on a Friday<br>night.
    </h1>

    <section class="paper">
      <svg width="1112" height="322" viewBox="0 0 1112 322" aria-hidden="true">
        <polygon fill="var(--paper-shadow)"
          points="0,18 40,22 80,12 130,26 180,16 230,30 290,20 340,34 400,44 460,52 520,60 580,56 640,66 700,60 760,72 820,64 880,74 940,66 1000,78 1060,70 1112,80 1112,322 0,322"/>
        <polygon fill="var(--paper)"
          points="0,26 45,30 90,20 140,34 185,24 240,38 295,28 345,42 405,52 465,58 525,68 585,62 645,74 705,66 765,80 825,72 885,82 945,74 1005,86 1065,78 1112,88 1112,322 0,322"/>
      </svg>
      <div class="paper-copy">
        <p class="intro">As a fitness trainer for men, I figured if you wanted Tits &amp; Ass I’d give it to you. At least long enough to make a buck and get my guys in shape.</p>
        <p class="pitch">You wanna lose weight? You wanna shrink that gut?<br>Touch me down here. I can help you shrink your gut.</p>
      </div>
    </section>
  </main>
</body>
</html>
```